Web Design Project

We need web design for a new baby products (nursery furniture) business in Australia.

The logo is already done, and I would like to reflect a similar theme throughout the website:
* Clean, white background.
* Use of lime green, purple and orange.
* Similar font to logo for headings
* FUNKY, FASHIONABLE, QUALITY feeling of website.

The main concept is to be attractive to discerning mums who are buying big items like a cot or chest of drawers. These are expensive items and will be considered the most important purchases for a newborn, so the website has to be enticing!!!
Updates

Hello,

Thank you for your submissions. I have received a few questions regarding the font and the coding of this website.

The job I am seeking is for design for an E-commerce store. The font was done by another pixel guild designer, so I do not know what type of font I am sorry.

I was hoping to have more designs by now, so please send them soon, this project is guaranteed!

I also ask you to read the brief properly please. The name of the business is Cradle Lane, as the logo says. The use of design that I have mentioned has only been demonstrated in a couple of designs submitted to me.

I look forward to seeing your work soon!

Kind Regards
Marla

Target Market(s)

Young mothers aged 25-45

Industry/Entity Type

Business

Requirements
Must have
• Must be funky, bright, energetic, attractive visually.
Nice to have
• I like the idea of some floral / design work in faded lime green, purple on some of the edges of different pages. Maybe islamic design? But has to be very fashionable.
Should not have
• Should not have any traditional ideas of baby websites.

ie- no stork, nappy images, teddybears etc.

```html
<!DOCTYPE html>
<html lang="en">
<head>
<meta charset="utf-8">
<title>Cradle Lane – Nursery Furniture</title>
<link rel="stylesheet" href="https://fonts.googleapis.com/css2?family=Cinzel:wght@600;700&family=Source+Sans+3:ital,wght@0,400;0,600;0,700;1,400&display=swap">
<style>
  :root {
    --page-dark: #1b1b1b;
    --pattern-mid: #3a3a3a;
    --white: #ffffff;
    --panel-fade: #eef0f0;
    --lime: #8cc414;
    --lime-dark: #6fa10a;
    --purple: #b536e0;
    --purple-bright: #c94bf0;
    --orange: #f7a21b;
    --ink: #2b2b2b;
    --ink-soft: #555555;
    --link-blue: #2a6ea6;
    --rule: #d4d6d6;
    --wood: #a0622a;
    --wood-dark: #3b2418;
    --cot-white: #e8ecef;
    --cot-lilac: #a9a6e8;
    --social-blue: #3b5998;
    --social-sky: #3fb7e8;
    --social-orange: #f28b1e;
    --sans: "Source Sans 3", "Myriad Pro", Arial, sans-serif;
    --serif: "Cinzel", "Trajan Pro", Georgia, serif;
  }
  * { box-sizing: border-box; margin: 0; padding: 0; }
  html, body { width: 1200px; height: 904px; overflow: hidden; }
  body { position: relative; background: var(--page-dark); font-family: var(--sans); color: var(--ink); }
  .abs { position: absolute; }

  .backdrop {
    position: absolute; inset: 0;
    background: radial-gradient(ellipse at 50% 45%, var(--pattern-mid) 0%, #2c2c2c 55%, var(--page-dark) 100%);
  }

  /* header */
  .header-panel {
    left: 341px; top: 8px; width: 517px; height: 315px;
    background: linear-gradient(180deg, var(--white) 0%, #f7f8f8 60%, var(--panel-fade) 100%);
  }
  .brand { left: 37px; top: 16px; display: flex; align-items: center; gap: 7px; }
  .brand-dot { width: 26px; height: 26px; border-radius: 50%; background: var(--lime); }
  .brand-name { font-family: var(--sans); font-weight: 700; font-size: 22px; color: var(--purple); line-height: 1; }
  .account-links { right: 43px; top: 14px; display: flex; gap: 13px; font-size: 8px; color: var(--ink-soft); white-space: nowrap; }
  .main-nav {
    left: 33px; top: 57px; width: 446px; height: 26px;
    display: flex; align-items: center; justify-content: space-between;
    font-family: var(--serif); font-size: 7px; font-weight: 700; color: var(--ink);
    white-space: nowrap;
  }
  .main-nav span { line-height: 1; }
  .main-nav .active {
    background: var(--purple); color: var(--white);
    height: 26px; padding: 0 5px; display: flex; align-items: center;
  }
  .nav-marker { left: 27px; top: 73px; width: 12px; height: 12px; border-radius: 50%; background: var(--orange); }
  .nav-rule { left: 33px; top: 88px; width: 444px; height: 1px; background: var(--rule); }

  .hero-arrow { top: 164px; }
  .hero-title { right: 282px; top: 114px; text-align: right; white-space: nowrap; }
  .hero-title .line-one { font-size: 25px; font-weight: 600; color: var(--purple-bright); font-variant: small-caps; line-height: 1; }
  .hero-title .line-two { font-size: 21px; font-weight: 400; color: var(--lime); line-height: 1.2; margin-top: 2px; }
  .hero-copy { right: 282px; top: 185px; text-align: right; font-size: 8.5px; font-weight: 600; line-height: 10.5px; color: var(--ink); white-space: nowrap; }
  .buy-button { left: 145px; top: 227px; width: 90px; height: 24px; border-radius: 6px; background: linear-gradient(180deg, #9bd21f, var(--lime-dark)); color: var(--white); font-size: 9px; font-weight: 700; display: flex; align-items: center; justify-content: center; }
  .hero-product { left: 252px; top: 117px; width: 218px; height: 178px; background: linear-gradient(160deg, #c57b36, var(--wood) 60%, #7a4318); border-radius: 6px; }

  /* newsletter */
  .newsletter { left: 333px; top: 333px; width: 535px; height: 26px; background: linear-gradient(180deg, #96cf1a, var(--lime-dark)); }
  .newsletter-text { left: 15px; top: 8px; font-size: 8px; font-weight: 700; color: var(--white); white-space: nowrap; }
  .subscribe-label { left: 283px; top: 5px; width: 60px; height: 17px; background: var(--purple); color: var(--white); font-size: 7px; font-weight: 700; display: flex; align-items: center; justify-content: center; letter-spacing: .3px; }
  .email-field { left: 343px; top: 5px; width: 108px; height: 17px; background: var(--white); font-size: 7px; font-style: italic; color: #888; padding: 4px 0 0 8px; }
  .social { top: 5px; width: 15px; height: 15px; border-radius: 2px; }

  /* products */
  .product-panel { left: 341px; top: 369px; width: 517px; height: 336px; background: var(--white); }
  .card { width: 116px; height: 152px; background: linear-gradient(180deg, var(--white) 55%, #eef1f1 100%); overflow: hidden; }
  .card-flag { position: absolute; left: 0; top: 0; }
  .card-image { position: absolute; left: 12px; top: 26px; width: 92px; height: 86px; border-radius: 4px; }
  .card-title { position: absolute; left: 10px; top: 113px; width: 100px; font-size: 8px; font-weight: 700; color: var(--link-blue); line-height: 9.5px; }
  .card-price { position: absolute; right: 15px; top: 133px; font-size: 8.5px; font-weight: 700; color: var(--ink); white-space: nowrap; }
  .card-price small { font-size: 6px; font-weight: 600; margin-left: 3px; }
  .shade-band { left: 341px; top: 705px; width: 519px; height: 13px; background: linear-gradient(90deg, #050505, #333 55%, #050505); }

  /* footer */
  .footer-col { top: 743px; width: 96px; }
  .footer-col h3 { font-size: 9px; font-weight: 700; color: var(--lime); line-height: 10px; margin-bottom: 14px; }
  .footer-col p { font-size: 7px; font-weight: 700; color: var(--white); line-height: 14.5px; white-space: nowrap; }
  .bottom-bar { left: 0; top: 848px; width: 1200px; height: 56px; background: #1a1a1a; }
  .bottom-brand { left: 348px; top: 17px; display: flex; align-items: center; gap: 5px; font-size: 11px; font-weight: 700; color: #9a9a9a; }
  .bottom-brand i { width: 14px; height: 14px; border-radius: 50%; background: #8a8a8a; display: block; }
  .bottom-text { top: 22px; font-size: 7px; color: #b8b8b8; white-space: nowrap; }
  .bottom-links { left: 706px; top: 22px; display: flex; gap: 12px; font-size: 7px; font-weight: 700; color: var(--white); white-space: nowrap; }
</style>
</head>
<body>
  <div class="backdrop" role="img" aria-label="Dark grey damask floral wallpaper pattern"></div>

  <header class="abs header-panel">
    <div class="abs brand"><span class="brand-dot"></span><span class="brand-name">Cradle Lane</span></div>
    <nav class="abs account-links"><span>Sign up</span><span>Login</span><span>My Account</span><span>Shopping Cart</span></nav>
    <nav class="abs main-nav">
      <span class="active">BABY GEAR</span><span>BATH</span><span>FURNITURE</span><span>HEALTH</span><span>LEARNING</span><span>NURSERY</span><span>CLOTHING</span><span>FAQ</span><span>CONTACT</span>
    </nav>
    <span class="abs nav-marker"></span>
    <div class="abs nav-rule"></div>

    <svg class="abs hero-arrow" style="left:14px" width="13" height="63" viewBox="0 0 13 63"><polygon points="13,0 13,63 0,31.5" fill="#8cc414"/></svg>
    <svg class="abs hero-arrow" style="left:494px" width="13" height="63" viewBox="0 0 13 63"><polygon points="0,0 0,63 13,31.5" fill="#8cc414"/></svg>

    <div class="abs hero-title">
      <div class="line-one">Shop Clearance</div>
      <div class="line-two">and Closeouts</div>
    </div>
    <p class="abs hero-copy">Save on all baby bath products and furniture<br>for a limited time.&nbsp; Buy any product over<br>300dlls and get a free 50dlls gift card.</p>
    <div class="abs buy-button">BUY NOW</div>
    <div class="abs hero-product" role="img" aria-label="Photo of a honey-toned wooden baby cot with white mattress"></div>
  </header>

  <section class="abs newsletter">
    <p class="abs newsletter-text">Subscribe to our monthly newsletter and get exclusive offers by email</p>
    <div class="abs subscribe-label">SUBSCRIBE</div>
    <div class="abs email-field">enter email address</div>
    <span class="abs social" style="left:464px;background:var(--social-blue)"></span>
    <span class="abs social" style="left:481px;background:var(--social-sky)"></span>
    <span class="abs social" style="left:498px;background:var(--social-orange)"></span>
  </section>

  <main class="abs product-panel">
    <article class="abs card" style="left:12px;top:11px">
      <svg class="card-flag" width="43" height="43"><polygon points="0,0 43,0 0,43" fill="#8cc414"/></svg>
      <div class="card-image" role="img" aria-label="Photo of a dark espresso sleigh cot with drawer" style="background:linear-gradient(160deg,#5a3a2c,var(--wood-dark))"></div>
      <p class="card-title">Lorem ipsum dolor sit amet consectetur</p>
      <p class="card-price">$ 585<small>USD</small></p>
    </article>
    <article class="abs card" style="left:139px;top:11px">
      <svg class="card-flag" width="43" height="43"><polygon points="0,0 43,0 0,43" fill="#8cc414"/></svg>
      <div class="card-image" role="img" aria-label="Photo of a lilac and white cot with storage drawer" style="background:linear-gradient(160deg,#d9d8f5,var(--cot-lilac))"></div>
      <p class="card-title">Lorem ipsum dolor sit amet consectetur</p>
      <p class="card-price">$ 585<small>USD</small></p>
    </article>
    <article class="abs card" style="left:266px;top:11px">
      <svg class="card-flag" width="43" height="43"><defs><linearGradient id="flagPurple" x1="0" y1="0" x2="1" y2="1"><stop offset="0" stop-color="#e070f5"/><stop offset="1" stop-color="#b536e0"/></linearGradient></defs><polygon points="0,0 43,0 0,43" fill="url(#flagPurple)"/></svg>
      <div class="card-image" role="img" aria-label="Photo of a honey wooden cot" style="background:linear-gradient(160deg,#c57b36,var(--wood))"></div>
      <p class="card-title">Lorem ipsum dolor sit amet consectetur</p>
      <p class="card-price">$ 585<small>USD</small></p>
    </article>
    <article class="abs card" style="left:392px;top:11px">
      <svg class="card-flag" width="43" height="43"><polygon points="0,0 43,0 0,43" fill="url(#flagPurple)"/></svg>
      <div class="card-image" role="img" aria-label="Photo of a white painted cot" style="background:linear-gradient(160deg,#f6f7f8,var(--cot-white))"></div>
      <p class="card-title">Lorem ipsum dolor sit amet consectetur</p>
      <p class="card-price">$ 585<small>USD</small></p>
    </article>
    <article class="abs card" style="left:12px;top:171px">
      <svg class="card-flag" width="43" height="43"><polygon points="0,0 43,0 0,43" fill="#8cc414"/></svg>
      <div class="card-image" role="img" aria-label="Photo of a tall honey-oak chest of drawers" style="background:linear-gradient(160deg,#c98a48,#a2622a)"></div>
      <p class="card-title">Lorem ipsum dolor sit amet consectetur</p>
      <p class="card-price">$ 585<small>USD</small></p>
    </article>
    <article class="abs card" style="left:139px;top:171px">
      <svg class="card-flag" width="43" height="43"><polygon points="0,0 43,0 0,43" fill="#8cc414"/></svg>
      <div class="card-image" role="img" aria-label="Photo of a tall white chest of drawers" style="background:linear-gradient(160deg,#f7f7f8,#e1e3e6)"></div>
      <p class="card-title">Lorem ipsum dolor sit amet consectetur</p>
      <p class="card-price">$ 585<small>USD</small></p>
    </article>
    <article class="abs card" style="left:266px;top:171px">
      <svg class="card-flag" width="43" height="43"><polygon points="0,0 43,0 0,43" fill="#8cc414"/></svg>
      <div class="card-image" role="img" aria-label="Photo of a dark espresso chest of drawers" style="background:linear-gradient(160deg,#4a3328,#241611)"></div>
      <p class="card-title">Lorem ipsum dolor sit amet consectetur</p>
      <p class="card-price">$ 585<small>USD</small></p>
    </article>
    <article class="abs card" style="left:392px;top:171px">
      <svg class="card-flag" width="43" height="43"><polygon points="0,0 43,0 0,43" fill="#8cc414"/></svg>
      <div class="card-image" role="img" aria-label="Photo of a wide dark brown dresser" style="background:linear-gradient(160deg,#5c3f33,#33211a)"></div>
      <p class="card-title">Lorem ipsum dolor sit amet consectetur</p>
      <p class="card-price">$ 585<small>USD</small></p>
    </article>
  </main>
  <div class="abs shade-band"></div>

  <footer>
    <div class="abs footer-col" style="left:365px">
      <h3>Lorem ipsum dolor sit amet consectetur</h3>
      <p>Lorem ipsum dolor sit amet</p><p>ipsum dolor sit amet</p><p>sit amet dolor ipsum et quid</p>
    </div>
    <div class="abs footer-col" style="left:487px">
      <h3>Ipsum dolor sit amet consectetur</h3>
      <p>dolor sit amet ipsum</p><p>Consectetur sit amet</p><p>Lorem ipsum</p>
    </div>
    <div class="abs footer-col" style="left:615px">
      <h3>dolor sit amet quid et se consectetur</h3>
      <p>Lorem dolor sit amet</p><p>ipsum et dolor quid un fac</p><p>dolor ipsum et quid</p>
    </div>
    <div class="abs footer-col" style="left:742px">
      <h3>Lorem ipsum dolor sit amet consectetur</h3>
      <p>Lorem ipsum dolor sit amet</p><p>ipsum dolor</p><p>Consectetur quid und fac</p>
    </div>

    <div class="abs bottom-bar">
      <div class="abs bottom-brand"><i></i>Cradle Lane</div>
      <p class="abs bottom-text" style="left:448px">Privacy Policy &nbsp;&nbsp;|&nbsp;&nbsp; Sitemap</p>
      <p class="abs bottom-text" style="left:593px">Copyright 2012</p>
      <nav class="abs bottom-links"><span>Sign up</span><span>Login</span><span>My Account</span><span>Shopping Cart</span></nav>
    </div>
  </footer>
</body>
</html>
```